Upscale square business card for photographer

I need the logo I already own designed into a card that features a photo on one side and text on the other. I want a very upscale approach that can be printed on thick paper - maybe even letterpress.

Target Market(s)

Designers, artists, editors

Industry/Entity Type

Business

Contact Information for Business Card

Should be square and feature the text below

Font styles to use
Serif
Sans Serif

Requirements
Must have
• Following contact info:
• Neil Hartwick
• 253-417-2964
• neil@neilhartwick.net
Nice to have
• Mailing address
• 2716 Mill Cove Rd. NE #248
• Fern Hollow, WA 98412
Should not have
• Should be monochrome - no color

```html
<!DOCTYPE html>
<html lang="en">
<head>
<meta charset="utf-8">
<title>Neil Hartwick — Square Business Card</title>
<link href="https://fonts.googleapis.com/css2?family=Oswald:wght@400&family=Open+Sans:wght@400&display=swap" rel="stylesheet">
<style>
  :root {
    --backdrop: #8a8a8a;
    --card-white: #ffffff;
    --ink: #1c1c1c;
    --ink-soft: #3a3a3a;
    --photo-deep: #121212;
    --photo-mid: #2a2a2a;
    --photo-light: #d9d9d9;
  }
  * { margin: 0; padding: 0; box-sizing: border-box; }
  html, body {
    width: 1200px;
    height: 1200px;
    overflow: hidden;
    background: var(--backdrop);
  }
  .canvas {
    position: relative;
    width: 1200px;
    height: 1200px;
  }
  .card {
    position: absolute;
    width: 480px;
    height: 480px;
    box-shadow: 0 6px 18px rgba(0, 0, 0, 0.25);
  }
  .card--front {
    left: 110px;
    top: 110px;
    background: var(--photo-deep);
  }
  .card-photo {
    width: 100%;
    height: 100%;
    background:
      radial-gradient(ellipse 22% 26% at 36% 34%, var(--photo-light) 0%, rgba(217,217,217,0.35) 45%, rgba(217,217,217,0) 100%),
      linear-gradient(180deg, var(--photo-mid) 0%, var(--photo-deep) 100%);
  }
  .card--back {
    left: 610px;
    top: 610px;
    background: var(--card-white);
    display: flex;
    flex-direction: column;
    align-items: center;
    justify-content: center;
    text-align: center;
    padding-top: 20px;
  }
  .brand-name {
    font-family: "Oswald", sans-serif;
    font-weight: 400;
    font-size: 40px;
    letter-spacing: 8px;
    text-transform: uppercase;
    color: var(--ink);
    margin-right: -8px;
    margin-bottom: 34px;
  }
  .contact-icons {
    display: flex;
    gap: 8px;
    margin-bottom: 12px;
  }
  .contact-icons svg {
    width: 20px;
    height: 20px;
  }
  .contact-details {
    font-family: "Open Sans", sans-serif;
    font-weight: 400;
    font-size: 15px;
    line-height: 1.35;
    color: var(--ink-soft);
    font-style: normal;
  }
  .contact-details .address { margin-bottom: 6px; }
</style>
</head>
<body>
  <main class="canvas">
    <section class="card card--front">
      <div class="card-photo" role="img" aria-label="Black and white photograph of a white egret preening its spread wing while standing in dark water"></div>
    </section>

    <section class="card card--back">
      <h1 class="brand-name">Neil Hartwick</h1>

      <div class="contact-icons" aria-hidden="true">
        <svg viewBox="0 0 20 20">
          <circle cx="10" cy="10" r="9" fill="none" stroke="#1c1c1c" stroke-width="1.4"/>
          <path d="M10 4.5a3.3 3.3 0 0 0-3.3 3.3c0 2.4 3.3 6.4 3.3 6.4s3.3-4 3.3-6.4A3.3 3.3 0 0 0 10 4.5z" fill="#1c1c1c"/>
          <circle cx="10" cy="7.8" r="1.2" fill="#fff"/>
        </svg>
        <svg viewBox="0 0 20 20">
          <circle cx="10" cy="10" r="9" fill="none" stroke="#1c1c1c" stroke-width="1.4"/>
          <path d="M7.2 5.2l1.6-.3 1 2.4-1.1.9a6 6 0 0 0 2.4 2.9l1-1 2.3 1.1-.4 1.6c-3.6.6-7.9-4.2-6.8-7.6z" fill="#1c1c1c"/>
        </svg>
        <svg viewBox="0 0 20 20">
          <circle cx="10" cy="10" r="9" fill="none" stroke="#1c1c1c" stroke-width="1.4"/>
          <rect x="5.2" y="6.6" width="9.6" height="6.8" fill="#1c1c1c"/>
          <path d="M5.6 7l4.4 3.4L14.4 7" fill="none" stroke="#fff" stroke-width="1"/>
        </svg>
      </div>

      <address class="contact-details">
        <p class="address">2716 Mill Cove Rd. NE #248,<br>Fern Hollow, WA 98412</p>
        <p class="phone">253-417-2964</p>
        <p class="email">neil@neilhartwick.net</p>
      </address>
    </section>
  </main>
</body>
</html>
```